Creating the Look and Feel of an Elite Boutique Consulting Practice: Kestrel Advisory

Complete a professional website on Weebly. As part of the site, we are open to a new logo -- we have just launched. We put up a starter website that shows you the content and theme we are going for. But clearly we aren't professional web designers and we need your help. Check out our start at kestreladvisory.com

Target Market(s)

Fortune 500 Clients

Industry/Entity Type

Management Consulting

Logo Text

KESTREL Advisory

Number of Pages Required

4 page

Requirements
Must have
• I've already set us up on Weebly. I'd like to give the selected designer the log-in credentials and have the designer create it on Weebly, so we can maintain it through that service.

```html
<!DOCTYPE html>
<html lang="en">
<head>
<meta charset="utf-8">
<title>Kestrel Advisory</title>
<link href="https://fonts.googleapis.com/css2?family=Ubuntu:ital,wght@0,300;0,400;0,500;1,400&display=swap" rel="stylesheet">
<style>
:root{
  --ink:#222;
  --text:#555;
  --muted:#777;
  --line:#c9c9c9;
  --band:#efefef;
  --nav-active:#eeeeee;
  --hero:#5f5f5f;
  --caption-bg:rgba(230,230,230,.88);
  --tick:#1f6fa8;
  --white:#fff;
}
*{margin:0;padding:0;box-sizing:border-box}
html,body{width:798px;height:1200px;overflow:hidden;background:var(--white)}
body{position:relative;font-family:"Ubuntu",sans-serif;color:var(--text)}
.abs{position:absolute}
.site-header{left:0;top:0;width:798px;height:70px;background:var(--white)}
.brand{left:51px;top:19px;display:flex;align-items:center;gap:8px;font-size:22px;font-weight:500;color:var(--ink)}
.brand-mark{width:30px;height:30px;border-radius:50%;background:var(--tick)}
.nav{left:0;top:0;height:70px;width:798px}
.nav a{position:absolute;top:0;height:70px;line-height:70px;font-size:13px;color:var(--text);text-decoration:none;text-align:center}
.nav a.active{background:var(--nav-active)}
.hero{left:0;top:70px;width:798px;height:366px;background:radial-gradient(ellipse at 50% 40%,#7a7a7a,#4e4e4e);border-top:1px dashed #bbb;border-bottom:1px dashed #bbb}
.caption{left:116px;top:216px;width:566px;height:88px;background:var(--caption-bg);border-radius:3px;padding:5px}
.caption-inner{width:100%;height:100%;border:1px dashed #888;text-align:center}
.caption h1{font-weight:400;font-size:24px;color:#111;margin-top:10px}
.caption p{font-size:14px;color:#111;margin-top:4px}
.dots span{position:absolute;top:396px;width:12px;height:12px;border-radius:50%;background:#ddd;border:2px solid #666}
.dots span.on{background:#fff;border-color:#222}
.intro{left:0;top:468px;width:798px;text-align:center}
.intro h2{font-weight:400;font-size:21px;color:var(--ink)}
.intro p{font-size:14px;color:var(--ink);margin-top:5px}
.feature{width:200px;text-align:center}
.feature svg{display:block;margin:0 auto}
.feature h3{font-weight:400;font-size:12.5px;color:var(--ink);margin-top:12px}
.feature p{font-size:9px;line-height:13.8px;color:var(--muted);margin-top:3px}
.feature a{color:var(--muted)}
.band{left:0;top:786px;width:798px;height:306px;background:var(--band);border-top:1px dashed var(--line);border-bottom:1px dashed var(--line)}
.photo{left:51px;top:839px;width:222px;height:194px;background:linear-gradient(135deg,#e8e8e8,#9a8a7c 55%,#4a4440)}
.approach{left:337px;top:818px;width:410px}
.approach h4{font-weight:400;font-size:11px;color:var(--ink)}
.item{position:absolute;left:0;width:410px;padding-left:32px;font-size:9px;line-height:13.8px;color:var(--muted)}
.item svg{position:absolute;left:0;top:1px}
.item em{display:block;color:var(--ink)}
.more{position:absolute;left:0;top:224px;font-size:9px;font-style:italic;color:var(--ink)}
.more a{color:var(--muted)}
.footer-brand{left:0;top:1106px;width:798px;text-align:center}
.footer-brand h5{font-weight:400;font-size:18px;color:#444}
.footer-brand p{font-size:12px;color:var(--muted);margin-top:5px}
.legal{left:0;top:1168px;width:798px;height:32px;background:var(--band);border-top:1px dashed var(--line);text-align:center;font-size:8px;line-height:24px;color:var(--ink)}
.legal a{color:var(--ink)}
</style>
</head>
<body>
<header class="abs site-header">
  <div class="abs brand"><span class="brand-mark"></span>Kestrel Advisory</div>
  <nav class="abs nav">
    <a class="active" href="#" style="left:478px;width:58px">About us</a>
    <a href="#" style="left:556px;width:68px">Approach</a>
    <a href="#" style="left:640px;width:46px">Team</a>
    <a href="#" style="left:696px;width:54px">Contact</a>
  </nav>
</header>

<section class="abs hero" role="img" aria-label="Photo of a businessman facing a chalkboard covered with arrows pointing in many directions"></section>
<div class="abs caption"><div class="caption-inner">
  <h1>Do you need to transform your organization?</h1>
  <p>Let's chart your path to success.</p>
</div></div>
<div class="dots"><span class="on" style="left:371px"></span><span style="left:392px"></span><span style="left:413px"></span></div>

<section class="abs intro">
  <h2>KESTREL ADVISORY</h2>
  <p>We help your organization achieve a successful, resilient transformation by:</p>
</section>

<div class="abs feature" style="left:63px;top:534px">
  <svg width="96" height="106" viewBox="0 0 96 106"><polygon points="48,3 92,27 92,79 48,103 4,79 4,27" fill="#fff" stroke="#ccc" stroke-width="4" stroke-linejoin="round"/>
  <path d="M35,32h26v8c0,9-6,15-13,15s-13-6-13-15z M44,55h8v7h-8z M38,62h20v5H38z" fill="#222"/>
  <path d="M35,35h-6c0,6 3,10 8,11 M61,35h6c0,6-3,10-8,11" fill="none" stroke="#222" stroke-width="2.5"/>
  <path d="M30,70h36l-4,5 4,5H30l4-5z" fill="#222"/></svg>
  <h3>Experienced.</h3>
  <p>Over the past three decades, we have deep experience driving organizational transformation in more than 33 countries, for some of the world's largest, most transformative companies in your industry.</p>
</div>

<div class="abs feature" style="left:298px;top:534px">
  <svg width="96" height="106" viewBox="0 0 96 106"><polygon points="48,3 92,27 92,79 48,103 4,79 4,27" fill="#fff" stroke="#ccc" stroke-width="4" stroke-linejoin="round"/>
  <text x="48" y="67" text-anchor="middle" font-family="Ubuntu,sans-serif" font-weight="500" font-size="40" fill="#aaa">?</text></svg>
  <h3>Curious.</h3>
  <p>Each of the dozens of transformations we've enabled are unique. Our most relevant experience is our ability to listen and learn where you want to go, and to partner with you to create an original set of tools and experiences to help your people get there. If you're curious, learn more about our <a href="#">team</a>.</p>
</div>

<div class="abs feature" style="left:536px;top:534px">
  <svg width="96" height="106" viewBox="0 0 96 106"><polygon points="48,3 92,27 92,79 48,103 4,79 4,27" fill="#fff" stroke="#ccc" stroke-width="4" stroke-linejoin="round"/>
  <rect x="31" y="48" width="8" height="18" fill="#aaa"/>
  <path d="M42,48l8-14c3-1 5,1 4,5l-2,7h9c3,0 4,3 3,5l-3,13c-1,2-2,2-4,2H42z" fill="#aaa"/></svg>
  <h3>Ready to Hear Your Story.</h3>
  <p>Of course the best way to get to know more about us is to <a href="#">contact us</a>, get to know us, and see what you think.</p>
</div>

<section class="abs band"></section>
<div class="abs photo" role="img" aria-label="Photo of a consulting team meeting around a conference table"></div>

<div class="abs approach">
  <h4>We help your organization achieve a successful, resilient transformation by:</h4>
  <div class="item" style="top:35px"><svg width="26" height="26" viewBox="0 0 26 26"><circle cx="12" cy="14" r="10" fill="none" stroke="var(--tick)" stroke-width="3"/><path d="M7,13l5,6 11-16" fill="none" stroke="#1a3550" stroke-width="3"/></svg>Partnering with you to clarify and communicate your transformational purpose.<em>Where are you going? What will you become? Why change now?</em></div>
  <div class="item" style="top:76px"><svg width="26" height="26" viewBox="0 0 26 26"><circle cx="12" cy="14" r="10" fill="none" stroke="var(--tick)" stroke-width="3"/><path d="M7,13l5,6 11-16" fill="none" stroke="#1a3550" stroke-width="3"/></svg>Assessing the current state of your organization.<em>Where are you today? What should be protected and preserved? What needs to change?</em></div>
  <div class="item" style="top:118px"><svg width="26" height="26" viewBox="0 0 26 26"><circle cx="12" cy="14" r="10" fill="none" stroke="var(--tick)" stroke-width="3"/><path d="M7,13l5,6 11-16" fill="none" stroke="#1a3550" stroke-width="3"/></svg>Building innovative engagements to help people master the skillets and mindsets needed for your current and future context.<em>What programs and projects should be created to ensure your leaders are ready, willing, able and excited to lead the transformation?</em></div>
  <div class="item" style="top:188px"><svg width="26" height="26" viewBox="0 0 26 26"><circle cx="12" cy="14" r="10" fill="none" stroke="var(--tick)" stroke-width="3"/><path d="M7,13l5,6 11-16" fill="none" stroke="#1a3550" stroke-width="3"/></svg>Embedding routines and practices to ensure the transformation is structurally resilient.<em>How should future work be divided, done and measured?</em></div>
  <p class="more">More about our <a href="#">approach.</a></p>
</div>

<footer class="abs footer-brand">
  <h5>KESTREL ADVISORY</h5>
  <p>Purpose-Led Organizational Transformation</p>
</footer>
<div class="abs legal">© 2015 <a href="#">KESTREL ADVISORY</a>. All Rights Reserved.</div>
</body>
</html>
```